Business Card Design Project

I require a business card design that looks professional for a small building company. Calloway Builders is the name of the company and i don't want to use a house or building design for a logo. I require a logo design for the card incorporating the name Calloway Builders but designed smartly.

We are a Registered Building Practitioner so the small logo attached must also be used on the card.

We cover a large range of Building / Construction, Concrete, Steelwork. Not sure how to implement this.

Colors are flexible, maybe a dark grey background with white writting over it, but i am keen to see other options.

Thanks.

Target Market(s)

Anyone

Industry/Entity Type

Building

Requirements
Must have
• The logo attached must be incorporated - can be small
A logo for my company needs to be included - using Calloway Builders as the base with no picture of a house or buildings.

```html
<!DOCTYPE html>
<html lang="en">
<head>
<meta charset="utf-8">
<title>Calloway Builders – Business Card Options</title>
<link rel="stylesheet" href="https://fonts.googleapis.com/css2?family=Exo+2:wght@400;700;800&display=swap">
<style>
  :root {
    --navy: #00234a;
    --steel: #999999;
    --white: #ffffff;
    --label: #222222;
    --sheet: #ffffff;
  }
  * { margin: 0; padding: 0; box-sizing: border-box; }
  html, body {
    width: 1200px; height: 730px; overflow: hidden;
    background: var(--sheet);
  }
  .sheet { position: relative; width: 1200px; height: 730px; }

  .option-label {
    position: absolute;
    font-family: "Exo 2", sans-serif;
    font-weight: 800;
    font-size: 13px;
    line-height: 13px;
    color: var(--label);
  }

  .card {
    position: absolute;
    width: 587px;
    height: 346px;
    color: var(--white);
    font-family: "Exo 2", sans-serif;
  }
  .card--navy { background: var(--navy); }
  .card--steel { background: var(--steel); }

  .card--back   { left: 0;   top: 14px; }
  .card--front  { left: 613px; top: 14px; }
  .card--single-navy  { left: 0;   top: 384px; }
  .card--single-steel { left: 613px; top: 384px; }

  .practitioner-badge {
    position: absolute;
    border: 2px solid var(--white);
    border-radius: 48px;
    background: rgba(255,255,255,0.12);
  }
  .card--back .practitioner-badge { left: 128px; top: 139px; width: 332px; height: 96px; }
  .practitioner-badge--small { left: 28px; top: 26px; width: 194px; height: 58px; border-radius: 29px; border-width: 1.5px; }

  .wordmark {
    position: absolute;
    left: 0; right: 0;
    text-align: center;
    font-weight: 700;
    text-transform: uppercase;
    white-space: nowrap;
    line-height: 1;
  }
  .card--front .wordmark { top: 156px; font-size: 31px; letter-spacing: 2px; }
  .card--single-navy .wordmark { top: 163px; font-size: 31px; letter-spacing: 2px; }
  .wordmark--stacked { top: 138px; }
  .wordmark--stacked span { display: block; }
  .wordmark--stacked .wordmark-line-top { font-size: 38px; letter-spacing: 1px; }
  .wordmark--stacked .wordmark-line-bottom { font-size: 50px; letter-spacing: 1px; margin-top: -2px; }

  .services {
    position: absolute;
    left: 0; right: 0;
    text-align: center;
    font-weight: 400;
    text-transform: uppercase;
    white-space: nowrap;
  }
  .card--front .services { top: 260px; font-size: 17px; letter-spacing: 0.4px; }
  .card--single-navy .services { top: 296px; font-size: 17px; letter-spacing: 0.4px; }
  .card--single-steel .services { top: 300px; font-size: 14px; letter-spacing: 1.2px; }
  .services .divider { padding: 0 4px; }
</style>
</head>
<body>
<main class="sheet">

  <span class="option-label" style="left:0; top:0;">Back</span>
  <span class="option-label" style="left:613px; top:0;">Front</span>
  <span class="option-label" style="left:0; top:368px;">Single Side</span>
  <span class="option-label" style="left:622px; top:368px;">Single Side</span>

  <section class="card card--navy card--back">
    <div class="practitioner-badge" role="img" aria-label="Registered building practitioner badge"></div>
  </section>

  <section class="card card--steel card--front">
    <h1 class="wordmark">Calloway Builders</h1>
    <p class="services">Building<span class="divider">|</span>Construction<span class="divider">|</span>Concrete<span class="divider">|</span>Steelwork</p>
  </section>

  <section class="card card--navy card--single-navy">
    <div class="practitioner-badge practitioner-badge--small" role="img" aria-label="Registered building practitioner badge"></div>
    <h2 class="wordmark">Calloway Builders</h2>
    <p class="services">Building<span class="divider">|</span>Construction<span class="divider">|</span>Concrete<span class="divider">|</span>Steelwork</p>
  </section>

  <section class="card card--steel card--single-steel">
    <div class="practitioner-badge practitioner-badge--small" role="img" aria-label="Registered building practitioner badge"></div>
    <h2 class="wordmark wordmark--stacked">
      <span class="wordmark-line-top">Calloway</span>
      <span class="wordmark-line-bottom">Builders</span>
    </h2>
    <p class="services">Building<span class="divider">|</span>Construction<span class="divider">|</span>Concrete<span class="divider">|</span>Steelwork</p>
  </section>

</main>
</body>
</html>
```